Financial Advisor needs a NEW business card design

We need a new card design as our current design has no white space and clients tend to want to write on the card. I am attaching our current logos and current card design. I have also played with some designs I liked online but don't have the knowledge (or software) to complete the designs in a format that is appropriate for production. I've attached those designs that I liked too. With two office locations and a disclaimer there is a lot of info but we want it to look tidy. We like the deep, rich blue colors and want it to look clean, strong, and modern yet classic.
Business
Included in the attached files

```html
<!DOCTYPE html>
<html lang="en">
<head>
<meta charset="utf-8">
<title>Norvale Financial Advisory – Business Card</title>
<link rel="stylesheet" href="https://fonts.googleapis.com/css2?family=Libre+Baskerville&family=Rajdhani:wght@600&family=Open+Sans:wght@400;600&display=swap">
<style>
  :root {
    --backdrop: #d8d6d2;
    --card-face: #fbfbfa;
    --card-edge: #e2e2e0;
    --band-deep: #10295a;
    --band-rich: #1a3d7c;
    --band-line: #7d98c8;
    --icon-fill: #eef2f8;
    --icon-mark: #12305e;
    --text-light: #ffffff;
    --text-dark: #1c2a44;
    --text-muted: #5a6478;
    --brand-ink: #12305e;
    --silver-1: #f7f8fa;
    --silver-2: #bfc5cf;
    --silver-3: #e4e7ec;
    --social-fill: #12305e;
  }
  * { box-sizing: border-box; margin: 0; padding: 0; }
  html, body { width: 1200px; height: 769px; overflow: hidden; }
  body { background: var(--backdrop); position: relative; }

  .card {
    position: absolute; left: 150px; top: 110px;
    width: 900px; height: 550px;
    background: var(--card-face);
    border: 1px solid var(--card-edge);
    box-shadow: 0 10px 30px rgba(0,0,0,0.18);
    overflow: hidden;
  }

  .brand {
    position: absolute; top: 34px; left: 0; width: 100%;
    text-align: center;
    font-family: "Libre Baskerville", serif;
    color: var(--brand-ink);
  }
  .brand-name { font-size: 58px; line-height: 1; letter-spacing: 1px; }
  .brand-tagline { font-size: 19px; letter-spacing: 2px; margin-top: 10px; }

  .contact-band {
    position: absolute; top: 150px; left: 0; width: 100%; height: 200px;
    background: linear-gradient(180deg, var(--band-rich) 0%, var(--band-deep) 100%);
    border-top: 3px solid var(--band-line);
    border-bottom: 3px solid var(--band-line);
  }
  .contact-col {
    position: absolute; top: 32px; width: 280px; margin-left: -140px;
    text-align: center; color: var(--text-light);
  }
  .col-person { left: 170px; }
  .col-web { left: 450px; }
  .col-phone { left: 730px; }
  .contact-icon { width: 60px; height: 60px; display: block; margin: 0 auto 16px; }

  .person-name {
    font-family: "Rajdhani", sans-serif; font-weight: 600;
    font-size: 32px; line-height: 1; letter-spacing: 1px;
  }
  .person-role {
    font-family: "Open Sans", sans-serif; font-size: 11px;
    letter-spacing: 1px; margin-top: 6px;
  }
  .contact-line {
    font-family: "Open Sans", sans-serif; font-size: 18px;
    line-height: 25px; letter-spacing: 0.3px;
  }

  .offices {
    position: absolute; top: 372px; left: 88px; right: 88px;
    display: flex; justify-content: space-between;
    font-family: "Open Sans", sans-serif; color: var(--text-dark);
  }
  .office-title {
    font-weight: 600; font-size: 13px; letter-spacing: 1.5px;
    color: var(--brand-ink); margin-bottom: 3px;
  }
  .office-line { font-size: 13px; line-height: 18px; }
  .office-right { text-align: right; }

  .disclaimer {
    position: absolute; top: 440px; left: 88px; right: 88px;
    font-family: "Open Sans", sans-serif; font-size: 10px;
    line-height: 13px; color: var(--text-muted); text-align: center;
  }

  .social-strip {
    position: absolute; top: 466px; left: 0; width: 100%; height: 66px;
    background: linear-gradient(90deg, var(--silver-2) 0%, var(--silver-1) 30%, var(--silver-3) 60%, var(--silver-2) 100%);
    border-top: 2px solid var(--band-line);
  }
  .follow-title {
    position: absolute; left: 88px; top: 12px;
    font-family: "Open Sans", sans-serif; font-weight: 600;
    font-size: 20px; letter-spacing: 2px; color: var(--brand-ink);
  }
  .follow-sub {
    position: absolute; left: 88px; top: 42px;
    font-family: "Open Sans", sans-serif; font-size: 9px;
    letter-spacing: 1px; color: var(--text-dark);
  }
  .social-list { position: absolute; left: 302px; top: 20px; display: flex; gap: 30px; }
  .social-item { width: 24px; height: 24px; background: var(--social-fill); border-radius: 3px; }
</style>
</head>
<body>
  <main class="card">
    <header class="brand">
      <div class="brand-name">Norvale</div>
      <div class="brand-tagline">FINANCIAL ADVISORY</div>
    </header>

    <section class="contact-band">
      <div class="contact-col col-person">
        <svg class="contact-icon" viewBox="0 0 70 70" aria-hidden="true">
          <circle cx="35" cy="35" r="33" fill="var(--icon-fill)"/>
          <rect x="20" y="18" width="30" height="34" rx="3" fill="var(--icon-mark)"/>
          <circle cx="35" cy="30" r="6" fill="var(--icon-fill)"/>
          <path d="M25 48 q10 -14 20 0 z" fill="var(--icon-fill)"/>
        </svg>
        <div class="person-name">DANIEL HARTLEY</div>
        <div class="person-role">GENERAL MANAGER</div>
      </div>

      <div class="contact-col col-web">
        <svg class="contact-icon" viewBox="0 0 70 70" aria-hidden="true">
          <circle cx="35" cy="35" r="33" fill="var(--icon-fill)"/>
          <g fill="none" stroke="var(--icon-mark)" stroke-width="2.5">
            <circle cx="35" cy="35" r="17"/>
            <ellipse cx="35" cy="35" rx="7" ry="17"/>
            <line x1="18" y1="35" x2="52" y2="35"/>
            <path d="M21 26 h28 M21 44 h28"/>
          </g>
        </svg>
        <div class="contact-line">hello@norvaleadvisory.com</div>
        <div class="contact-line">www.norvaleadvisory.com</div>
      </div>

      <div class="contact-col col-phone">
        <svg class="contact-icon" viewBox="0 0 70 70" aria-hidden="true">
          <circle cx="35" cy="35" r="33" fill="var(--icon-fill)"/>
          <rect x="25" y="16" width="20" height="38" rx="3" fill="none" stroke="var(--icon-mark)" stroke-width="2.5"/>
          <rect x="28" y="21" width="14" height="24" fill="var(--icon-mark)"/>
          <circle cx="35" cy="49.5" r="1.8" fill="var(--icon-mark)"/>
        </svg>
        <div class="contact-line">020 481 7356</div>
        <div class="contact-line">020 481 7357</div>
      </div>
    </section>

    <section class="offices">
      <div class="office office-left">
        <div class="office-title">CITY OFFICE</div>
        <div class="office-line">Level 4, 18 Harbour Lane, Eastbridge</div>
      </div>
      <div class="office office-right">
        <div class="office-title">NORTH OFFICE</div>
        <div class="office-line">7 Millstone Road, Ashford Park</div>
      </div>
    </section>

    <p class="disclaimer">Norvale Financial Advisory is an authorised representative. Advice given is general in nature and does not consider your personal circumstances.</p>

    <footer class="social-strip">
      <div class="follow-title">FOLLOW US</div>
      <div class="follow-sub">ON SOCIAL NETWORKS</div>
      <div class="social-list">
        <span class="social-item"></span>
        <span class="social-item"></span>
        <span class="social-item"></span>
        <span class="social-item"></span>
      </div>
    </footer>
  </main>
</body>
</html>
```